Eye Grabbing - Travel Consultant Business Card

I need a business card that stands out. Vertical instead of horizontal, rounded edges, would love to use the same layout item for magnets. I have uploaded my current logo and tag line. Would love a cool eye-grabbing image for the front side. Can be something different than what you see on my website as I am looking to rebrand as a Leisure, Luxury & Adventure Specialist.

Target Market(s)

Leisure and Luxury Travel

Industry/Entity Type

Travel Agent

Contact Information for Business Card

Company Name - uMbrela Travel; Name - Rhoda Peverell; Title - Travel Consultant; Website - www.umbrelatravel.example ; Phone: 318-662-0951 Email rhoda@umbrelatravel.example and my facebook, twitter, and Instagram handles

Font styles to use
Serif

Colors

Designer to choose colors to be used in the design.

Requirements
Must have
• my tag line of -- Dream Explore Discover
Nice to have

```html
<!DOCTYPE html>
<html lang="en">
<head>
<meta charset="utf-8">
<title>uMbrela Travel – Business Card</title>
<link href="https://fonts.googleapis.com/css2?family=Roboto:wght@400;500;700&family=Montserrat:wght@600&display=swap" rel="stylesheet">
<style>
  :root {
    --backdrop: #dcdcdc;
    --white: #ffffff;
    --lime: #d3da4c;
    --leaf: #7cc851;
    --green: #30ae53;
    --teal: #1f7f6c;
    --navy: #2d3a8f;
    --arc-blue: #3a93b5;
    --brand-ink: #2d3a8f;
    --sun: #f2ec7e;
  }
  * { margin: 0; padding: 0; box-sizing: border-box; }
  html, body { width: 1200px; height: 1200px; overflow: hidden; }
  body { background: var(--backdrop); position: relative; font-family: "Roboto", sans-serif; }

  .card {
    position: absolute;
    top: 226px;
    width: 392px;
    height: 686px;
    border-radius: 22px;
    overflow: hidden;
  }
  .card-front { left: 195px; }
  .card-back {
    left: 660px;
    background: linear-gradient(180deg, var(--sun) 0%, #c9df6a 25%, #7cc85e 45%, var(--green) 62%, #228a6e 78%, #27588c 90%, var(--navy) 100%);
  }
  .front-bg { position: absolute; inset: 0; }

  .brand { position: absolute; left: 0; right: 0; top: 72px; text-align: center; }
  .brand-dot {
    display: block; margin: 0 auto 24px;
    width: 92px; height: 92px; border-radius: 50%;
    background: var(--green);
  }
  .brand-name {
    font-family: "Roboto", sans-serif; font-weight: 700;
    font-size: 30px; color: var(--brand-ink);
    text-transform: uppercase; letter-spacing: 1px;
  }

  .person { position: absolute; left: 0; right: 0; top: 452px; text-align: center; color: var(--white); }
  .person-name { font-weight: 700; font-size: 24px; letter-spacing: -0.5px; }
  .person-title { font-weight: 500; font-size: 17px; margin-top: 2px; }

  .contact { position: absolute; left: 0; right: 0; top: 526px; text-align: center; color: var(--white); font-size: 16px; line-height: 22.5px; }
  .contact-line { display: flex; justify-content: center; align-items: center; gap: 6px; }
  .contact-line svg { width: 14px; height: 14px; fill: var(--white); }

  .tagline {
    position: absolute; left: 0; right: 0; top: 632px; text-align: center;
    font-family: "Montserrat", sans-serif; font-weight: 600;
    font-size: 17px; letter-spacing: 4.5px; color: var(--white);
  }

  .social { position: absolute; left: 52px; top: 614px; display: flex; gap: 4px; }
  .social-dot { width: 31px; height: 31px; border-radius: 50%; }
  .social-dot:nth-child(1) { background: #e2e35a; }
  .social-dot:nth-child(2) { background: #66c254; }
  .social-dot:nth-child(3) { background: #2f9d66; }
</style>
</head>
<body>
  <section class="card card-front">
    <svg class="front-bg" viewBox="0 0 392 686" preserveAspectRatio="none">
      <defs>
        <linearGradient id="front-fill" x1="0" y1="0" x2="0" y2="1">
          <stop offset="0.35" stop-color="#d3da4c"/>
          <stop offset="0.58" stop-color="#7cc851"/>
          <stop offset="0.78" stop-color="#30ae53"/>
          <stop offset="0.9" stop-color="#1f7f6c"/>
          <stop offset="1" stop-color="#2d5a8a"/>
        </linearGradient>
      </defs>
      <rect width="392" height="686" fill="url(#front-fill)"/>
      <path d="M0,0 H392 V240 C370,320 300,392 200,392 C120,392 40,370 0,278 Z" fill="#ffffff"/>
      <path d="M0,278 C40,370 120,392 200,392 C300,392 370,320 392,240" fill="none" stroke="#3a93b5" stroke-width="6"/>
    </svg>

    <div class="brand">
      <span class="brand-dot"></span>
      <div class="brand-name">uMbrela Travel</div>
    </div>

    <div class="person">
      <div class="person-name">Rhoda Peverell</div>
      <div class="person-title">Travel Consultant</div>
    </div>

    <div class="contact">
      <div class="contact-line">
        <svg viewBox="0 0 24 24"><path d="M6.6 10.8a15 15 0 0 0 6.6 6.6l2.2-2.2c.3-.3.7-.4 1-.2 1.1.4 2.300.6 3.6.6.6 0 1 .4 1 1V20c0 .6-.4 1-1 1A17 17 0 0 1 3 4c0-.6.4-1 1-1h3.5c.6 0 1 .4 1 1 0 1.3.2 2.5.6 3.6.1.3 0 .7-.2 1z"/></svg>
        <span>318-662-0951</span>
      </div>
      <div class="contact-line">
        <svg viewBox="0 0 24 24"><path d="M2 5h20v14H2z M2 5l10 8 10-8" fill="none" stroke="#fff" stroke-width="2"/></svg>
        <span>rhoda@umbrelatravel.example</span>
      </div>
      <div class="contact-line">
        <svg viewBox="0 0 24 24"><circle cx="12" cy="12" r="9" fill="none" stroke="#fff" stroke-width="2"/><path d="M3 12h18M12 3c3 3 3 15 0 18M12 3c-3 3-3 15 0 18" fill="none" stroke="#fff" stroke-width="1.6"/></svg>
        <span>www.umbrelatravel.example</span>
      </div>
    </div>

    <div class="tagline">Dream. Explore. Discover</div>
  </section>

  <section class="card card-back">
    <div class="social" aria-label="Social media profiles">
      <span class="social-dot"></span>
      <span class="social-dot"></span>
      <span class="social-dot"></span>
    </div>
  </section>
</body>
</html>
```